Fresh new and cool frozen burger box! Come be a part of an amazing project!

Crust Fins and Melts restaurant is expanding into the frozen foods market!
please check out our website to understand the vibe of the company
https://brivanta.ca
this is a line of premium Halal meat, we want to stress our top-notch quality.
we like the orange colours so see what you can do with them. (maybe white and orange combo)
you have lots of creative freedom here, feel free to use the burger photo I am attaching or any image off the website.
logo should be nice and visible.
we want this packaging to really stand out and be special.
Come be a part of an amazing project!
Target Market(s)
Muslim Flails, looking of a quality meat burger. mostly already familiar with our brand
Industry/Entity Type
Frozen food
Look and feel

```html
<!DOCTYPE html>
<html lang="en">
<head>
<meta charset="utf-8">
<title>Brivanta Burger Patties – Box Dieline</title>
<link rel="stylesheet" href="https://fonts.googleapis.com/css2?family=Oswald:wght@500;700&family=Montserrat:wght@700&family=Passion+One:wght@700&display=swap">
<style>
  :root {
    --orange: #f7941d;
    --ink: #1b1c21;
    --red: #e21e26;
    --white: #ffffff;
    --fold: #e0312b;
    --stage: #ffffff;
  }
  html, body {
    margin: 0;
    padding: 0;
    width: 1200px;
    height: 648px;
    overflow: hidden;
    background: var(--stage);
  }
  .canvas {
    width: 1200px;
    height: 648px;
    display: flex;
    align-items: center;
    justify-content: center;
  }
  .dieline { height: 630px; width: auto; display: block; }
  .panel-orange { fill: var(--orange); stroke: var(--ink); stroke-width: 2; }
  .panel-ink { fill: var(--ink); }
  .fold { fill: none; stroke: var(--fold); stroke-width: 1.6; stroke-dasharray: 6 5; }
  .cut { fill: none; stroke: var(--ink); stroke-width: 2; }
  .brand-name { font-family: "Oswald", sans-serif; font-weight: 700; }
  .brand-on-ink { fill: var(--orange); }
  .brand-on-orange { fill: var(--white); }
  .brand-mark { fill: var(--white); stroke: var(--red); stroke-width: 3; }
  .tagline { font-family: "Montserrat", sans-serif; font-weight: 700; }
  .tagline-light { fill: var(--white); }
  .tagline-dark { fill: var(--ink); }
  .badge { fill: var(--red); }
  .badge-text { font-family: "Oswald", sans-serif; font-weight: 500; fill: var(--white); }
  .halal { font-family: "Passion One", sans-serif; font-weight: 700; }
  .halal-light { fill: var(--white); }
  .halal-dark { fill: var(--ink); }
  .bullets { font-family: "Oswald", sans-serif; font-weight: 500; fill: var(--ink); font-size: 13px; }
  .zigzag { fill: none; stroke: var(--ink); stroke-width: 1.4; }
</style>
</head>
<body>
<main class="canvas">
  <svg class="dieline" viewBox="100 65 885 1275" xmlns="http://www.w3.org/2000/svg">
    <defs>
      <linearGradient id="burger-tone" x1="0" y1="0" x2="0" y2="1">
        <stop offset="0" stop-color="#f2d3a8"/>
        <stop offset="0.35" stop-color="#e3a86a"/>
        <stop offset="0.5" stop-color="#b8432a"/>
        <stop offset="0.65" stop-color="#6b4a2e"/>
        <stop offset="0.8" stop-color="#5f9a3a"/>
        <stop offset="1" stop-color="#e9b676"/>
      </linearGradient>
      <linearGradient id="burger-tone-side" x1="0" y1="0" x2="1" y2="0">
        <stop offset="0" stop-color="#f2d3a8"/>
        <stop offset="0.35" stop-color="#e3a86a"/>
        <stop offset="0.55" stop-color="#b8432a"/>
        <stop offset="0.75" stop-color="#6b4a2e"/>
        <stop offset="1" stop-color="#5f9a3a"/>
      </linearGradient>
    </defs>

    <!-- Left side wall with flaps -->
    <g class="side-left">
      <polygon class="panel-orange" points="190,137 110,155 110,545 190,558"/>
      <polygon class="panel-orange" points="190,137 210,75 315,75 333,137"/>
      <polygon class="panel-orange" points="190,558 210,622 315,622 333,558"/>
      <rect class="panel-orange" x="190" y="137" width="143" height="421"/>
      <rect role="img" aria-label="Burger photo" x="215" y="455" width="115" height="103" rx="40" fill="url(#burger-tone-side)"/>
      <g transform="translate(248,300) rotate(-90)">
        <circle class="brand-mark" cx="-62" cy="-9" r="8"/>
        <text class="brand-name brand-on-orange" x="-50" y="0" font-size="26" textLength="94" lengthAdjust="spacingAndGlyphs">BRIVANTA</text>
        <rect class="badge" x="52" y="-18" width="40" height="32"/>
        <text class="badge-text" x="72" y="-5" font-size="10" text-anchor="middle">BURGER</text>
        <text class="badge-text" x="72" y="9" font-size="10" text-anchor="middle">PATTIES</text>
        <text class="tagline tagline-dark" x="-50" y="12" font-size="8" textLength="94" lengthAdjust="spacingAndGlyphs">Pizza • Burgers • Wings</text>
      </g>
      <text class="halal halal-dark" transform="translate(293,286) rotate(-90)" font-size="30" text-anchor="middle" textLength="172" lengthAdjust="spacingAndGlyphs">100% HALAL</text>
    </g>

    <!-- Right side wall with flaps -->
    <g class="side-right">
      <polygon class="panel-orange" points="895,137 975,155 975,545 895,558"/>
      <polygon class="panel-orange" points="753,137 770,75 878,75 895,137"/>
      <polygon class="panel-orange" points="753,558 770,622 878,622 895,558"/>
      <rect class="panel-orange" x="753" y="137" width="142" height="421"/>
      <rect role="img" aria-label="Burger photo" x="758" y="140" width="112" height="100" rx="40" fill="url(#burger-tone-side)"/>
      <g transform="translate(838,410) rotate(90)">
        <circle class="brand-mark" cx="-78" cy="-9" r="8"/>
        <text class="brand-name brand-on-orange" x="-66" y="0" font-size="26" textLength="98" lengthAdjust="spacingAndGlyphs">BRIVANTA</text>
        <rect class="badge" x="40" y="-18" width="40" height="32"/>
        <text class="badge-text" x="60" y="-5" font-size="10" text-anchor="middle">BURGER</text>
        <text class="badge-text" x="60" y="9" font-size="10" text-anchor="middle">PATTIES</text>
        <text class="tagline tagline-dark" x="-66" y="12" font-size="8" textLength="98" lengthAdjust="spacingAndGlyphs">Pizza • Burgers • Wings</text>
      </g>
      <text class="halal halal-dark" transform="translate(793,412) rotate(90)" font-size="30" text-anchor="middle" textLength="175" lengthAdjust="spacingAndGlyphs">100% HALAL</text>
    </g>

    <!-- Main column -->
    <rect class="panel-ink" x="333" y="137" width="420" height="756"/>
    <rect fill="var(--orange)" x="333" y="893" width="420" height="372"/>
    <path class="panel-orange" d="M333 1265 V1300 Q333 1330 363 1330 H723 Q753 1330 753 1300 V1265"/>
    <rect class="cut" x="333" y="137" width="420" height="1128"/>

    <!-- Back wall (upside down) -->
    <g class="back-wall" transform="rotate(180 543 629)">
      <circle class="brand-mark" cx="448" cy="607" r="12"/>
      <text class="brand-name brand-on-ink" x="464" y="624" font-size="34" textLength="120" lengthAdjust="spacingAndGlyphs">BRIVANTA</text>
      <rect class="badge" x="598" y="592" width="58" height="40"/>
      <text class="badge-text" x="627" y="609" font-size="13" text-anchor="middle">BURGER</text>
      <text class="badge-text" x="627" y="626" font-size="13" text-anchor="middle">PATTIES</text>
      <text class="tagline tagline-light" x="436" y="641" font-size="10" textLength="150" lengthAdjust="spacingAndGlyphs">Pizza • Burgers • Wings</text>
      <text class="halal halal-light" x="543" y="677" font-size="36" text-anchor="middle" textLength="222" lengthAdjust="spacingAndGlyphs">100% HALAL</text>
    </g>

    <!-- Lid top -->
    <g class="lid">
      <rect role="img" aria-label="Burger photo with bacon, cheese, tomato and lettuce" x="333" y="808" width="272" height="302" rx="60" fill="url(#burger-tone)"/>
      <circle class="brand-mark" cx="418" cy="758" r="15"/>
      <text class="brand-name brand-on-ink" x="440" y="777" font-size="44" textLength="148" lengthAdjust="spacingAndGlyphs">BRIVANTA</text>
      <text class="tagline tagline-light" x="399" y="795" font-size="14" textLength="190" lengthAdjust="spacingAndGlyphs">Pizza • Burgers • Wings</text>
      <rect class="badge" x="604" y="741" width="78" height="56"/>
      <text class="badge-text" x="643" y="765" font-size="19" text-anchor="middle">BURGER</text>
      <text class="badge-text" x="643" y="790" font-size="19" text-anchor="middle">PATTIES</text>
      <text class="halal halal-light" x="398" y="862" font-size="46" textLength="285" lengthAdjust="spacingAndGlyphs">100% HALAL</text>

      <polyline class="zigzag" points="610,928 615,924 620,928 625,924 630,928 635,924 640,928 645,924 650,928 655,924 660,928 665,924 670,928 675,924 680,928 685,924 690,928 695,924 700,928 705,924 710,928 715,924 720,928 725,924"/>
      <g class="bullets">
        <text x="623" y="960">• LOREM IPSUM</text>
        <text x="623" y="987">• DOLOR SIT AMET</text>
        <text x="623" y="1014">• CONSECTETUR</text>
        <text x="623" y="1041">• ADIPISCING ELI</text>
        <text x="623" y="1068">• TNEC DIAM DIGNI</text>
      </g>
      <polyline class="zigzag" points="610,1090 615,1086 620,1090 625,1086 630,1090 635,1086 640,1090 645,1086 650,1090 655,1086 660,1090 665,1086 670,1090 675,1086 680,1090 685,1086 690,1090 695,1086 700,1090 705,1086 710,1090 715,1086 720,1090 725,1086"/>
    </g>

    <!-- Front flap -->
    <g class="front-flap">
      <circle class="brand-mark" cx="443" cy="1162" r="11"/>
      <text class="brand-name brand-on-orange" x="460" y="1182" font-size="34" textLength="118" lengthAdjust="spacingAndGlyphs">BRIVANTA</text>
      <text class="tagline tagline-dark" x="428" y="1197" font-size="10" textLength="150" lengthAdjust="spacingAndGlyphs">Pizza • Burgers • Wings</text>
      <rect class="badge" x="590" y="1153" width="60" height="44"/>
      <text class="badge-text" x="620" y="1171" font-size="15" text-anchor="middle">BURGER</text>
      <text class="badge-text" x="620" y="1191" font-size="15" text-anchor="middle">PATTIES</text>
      <text class="halal halal-dark" x="540" y="1240" font-size="36" text-anchor="middle" textLength="224" lengthAdjust="spacingAndGlyphs">100% HALAL</text>
    </g>

    <!-- Fold lines -->
    <g class="folds">
      <line class="fold" x1="190" y1="137" x2="333" y2="137"/>
      <line class="fold" x1="753" y1="137" x2="895" y2="137"/>
      <line class="fold" x1="190" y1="558" x2="895" y2="558"/>
      <line class="fold" x1="190" y1="137" x2="190" y2="558"/>
      <line class="fold" x1="333" y1="137" x2="333" y2="558"/>
      <line class="fold" x1="753" y1="137" x2="753" y2="558"/>
      <line class="fold" x1="895" y1="137" x2="895" y2="558"/>
      <line class="fold" x1="333" y1="700" x2="753" y2="700"/>
      <line class="fold" x1="333" y1="1120" x2="753" y2="1120"/>
      <line class="fold" x1="345" y1="1265" x2="741" y2="1265"/>
    </g>
  </svg>
</main>
</body>
</html>
```